Tactical Supply Company needing memorable business card design

Our tactical supply comapny is in need of a new business card design that will set us apart from the amateurs. We sell tactical gear ranging from backpacks and range bags to apparel and other gear. We are looking for a sharp design that incorporates our logo, website, and name. Our colors are white, red, and black, or any combination of the three, preferably red and black.
I have attached our logo with our name underneath but I have also edited that design with the logo incorporated next to the name (attached).

Target Market(s)

Law enforcement, military, tactical

Industry/Entity Type

Business

Contact Information for Business Card

Include www.fernhollowprovisions-demo.com

Colors
000000
ec1f27
ffffff

Requirements
Must have
• Our name, logo, and website. This is intended to be a memorable simple card, no name, address, email, or phone number info is necessary. Designs that do include this additional info will still be considered if they are absolutely spectacular.
Should not have
• A standard template design, I can create that in my own on Cardvellum. I am looking for a new, creative design that is completely unique to my company.

```html
<!DOCTYPE html>
<html lang="en">
<head>
<meta charset="utf-8">
<title>Fern Hollow Provisions – Business Card</title>
<link href="https://fonts.googleapis.com/css2?family=Arimo:wght@400;700&display=swap" rel="stylesheet">
<style>
  :root {
    --page-bg: #2a2a2a;
    --card-black: #000000;
    --plate-dark: #0b0b0b;
    --plate-light: #1c1c1c;
    --brand-red: #ec1f27;
    --brand-white: #ffffff;
    --soft-white: #e6e6e6;
  }
  * { box-sizing: border-box; margin: 0; padding: 0; }
  html, body {
    width: 1200px;
    height: 1200px;
    overflow: hidden;
    background: var(--page-bg);
    font-family: "Arimo", Arial, sans-serif;
  }
  .stage {
    width: 1200px;
    height: 1200px;
    display: flex;
    align-items: center;
    justify-content: center;
  }
  .business-card {
    position: relative;
    width: 900px;
    height: 514px;
    background: var(--card-black);
    overflow: hidden;
  }
  .plate-texture {
    position: absolute;
    inset: 0;
    background: radial-gradient(ellipse at 40% 30%, var(--plate-light) 0%, var(--plate-dark) 70%);
  }
  .brand {
    position: absolute;
    left: 165px;
    top: 140px;
    display: flex;
    align-items: center;
    gap: 22px;
  }
  .brand-mark {
    width: 58px;
    height: 58px;
    background: var(--brand-red);
  }
  .brand-name {
    color: var(--brand-white);
    font-weight: 700;
    font-size: 50px;
    letter-spacing: 2px;
    text-transform: uppercase;
    line-height: 1;
  }
  .holder-name {
    position: absolute;
    left: 165px;
    top: 300px;
    color: var(--soft-white);
    font-size: 27px;
    letter-spacing: 1px;
  }
  .contact-list {
    position: absolute;
    left: 450px;
    top: 303px;
    list-style: none;
    color: var(--brand-red);
    font-size: 21px;
    line-height: 1.45;
  }
  .contact-list .phone { margin-bottom: 14px; font-size: 23px; }
</style>
</head>
<body>
  <main class="stage">
    <section class="business-card">
      <div class="plate-texture" role="img" aria-label="Black diamond-plate metal texture across the card"></div>
      <div class="brand">
        <span class="brand-mark"></span>
        <span class="brand-name">Fern Hollow Provisions</span>
      </div>
      <p class="holder-name">Dale Morrow</p>
      <ul class="contact-list">
        <li class="phone">555 014 782</li>
        <li class="email">dale.morrow@fernhollow-demo.com</li>
        <li class="website">www.fernhollowprovisions-demo.com</li>
      </ul>
    </section>
  </main>
</body>
</html>
```